Designer Instructions – Updated Referral Program Flyer

(Based on the mock-up in “Brief Layout and Instructions.pdf”)

OVERALL STYLE + LAYOUT

Maintain the same general layout, structure, and flow as the mock-up flyer (front and back).

This is an update of an older flyer, not a full redesign — keep the same sections, proportions, and overall visual feel, but with cleaner, more modern design improvements.

The final flyer should look clean, bold, professional, and high-impact, geared toward realtors, property managers, and contractors who refer work.

FRONT SIDE INSTRUCTIONS
1. Header Section

Remove the Tallow Ridge Builders logo from the top banner.
(Shown on page 1 of the PDF)

2. Main Headline

Keep the same three-line structure:
EARN
UNLIMITED
CASH

Center it, maximize impact, and increase the font size of CASH so all three words match in importance.

Make the headline bold, clean, and the main focal point.

3. Cash Incentive Box

Keep the "$500 minimum OR 10% per referral" box, but upgrade the graphics to look sharper and more modern.

Ensure the wording matches exactly what’s in the mock-up.

4. Premier Partner Program Ribbon

Clean up and modernize the "PREMIER PARTNER PROGRAM" bar while keeping the same position and structure.

Ensure the checkmark badge remains crisp and professional.

5. Supporting Icons Section

Keep the four icons/benefit boxes (Guaranteed Payout, Free Evaluations, Affordable Solutions, Industry Leaders) in the same order.

Update the icons to cleaner, more modern styles — but maintain the same meanings.

Improve alignment and spacing for sharper visual consistency.

6. Remove Icons in Contact Area

At the bottom (“CALL TEXT OR BOOK ONLINE 555-014-2796 TallowRidgeBuilders.example”), remove the phone and internet icons, as noted on page 2 of the PDF.

7. Replace All Images

I (Darnell) will provide all updated stock images separately via email.

Replace the flood/water-damage imagery and roof leak with the new images I send.

Keep image placement and proportions the same as the mock-up.

BACK SIDE INSTRUCTIONS
1. Header Image + “REFER / EARN” Section

Maintain the same large split-image layout (“The more you refer, the more you earn”).

Replace all background imagery with the new assets I will send.

Keep the CASH FLOW image section but modernize the type and spacing.

2. “HOW IT WORKS” Section

Preserve the three-column layout:

Refer Flood, Water & Mold Damage

We Take Care of Everything (evaluations/insurance)

Get Paid to Share

Update images, tighten spacing, and use modern iconography.

3. Remove Phone/Internet Icons

Same as the front side — remove small communication icons and keep only the text/number/URL.

4. Bottom Contact Bar

Keep the blue bar, same wording, same layout — just modernize the style if needed for clarity.

5. Replace All Back-Side Images

Again, I will email you the image assets.

Keep the layout EXACT — just update with higher-quality photos and improved design.

TEXT CONTENT (Keep as-is unless spacing adjustments needed)

All text shown in the PDF should remain exactly the same unless spacing or visual balance requires minor adjustments.
Example from page 3:

“REFER FLOOD, MOLD & CONSTRUCTION JOBS”

“We Schedule a Free Estimate. If Approved, You Get Paid.”

“Everybody Benefits From Referrals”

Everything stays, just refreshed and visually improved.

DESIGN GOALS

Flyer should look high-end and trustworthy, not salesy.

Consistent color theme: blues, whites, yellows, same palette as original.

Use bold, modern fonts with strong readability.

Ensure all headlines pop and all benefit boxes are clean, well-aligned, and evenly spaced.

The final result should feel like a premium referral program flyer for a top-tier restoration/remodel company.

FILES I WILL PROVIDE

I will send the designer:

All replacement stock photos

Any updated logos (if needed)

Original high-resolution version of the mock-up (if available)

Any additional icons preferred

0054AA
0677BA
7BADD7
CADEEF
E8F1F8

• Designer Instructions – Updated Referral Program Flyer (Based on the mock-up in “Brief Layout and Instructions.pdf”) OVERALL STYLE + LAYOUT Maintain the same general layout, structure, and flow as the mock-up flyer (front and back). This is an update of an older flyer, not a full redesign — keep the same sections, proportions, and overall visual feel, but with cleaner, more modern design improvements. The final flyer should look clean, bold, professional, and high-impact, geared toward realtors, property managers, and contractors who refer work. FRONT SIDE INSTRUCTIONS 1. Header Section Remove the Tallow Ridge Builders logo from the top banner. (Shown on page 1 of the PDF) 2. Main Headline Keep the same three-line structure: EARN UNLIMITED CASH Center it, maximize impact, and increase the font size of CASH so all three words match in importance. Make the headline bold, clean, and the main focal point. 3. Cash Incentive Box Keep the "$500 minimum OR 10% per referral" box, but upgrade the graphics to look sharper and more modern. Ensure the wording matches exactly what’s in the mock-up. 4. Premier Partner Program Ribbon Clean up and modernize the "PREMIER PARTNER PROGRAM" bar while keeping the same position and structure. Ensure the checkmark badge remains crisp and professional. 5. Supporting Icons Section Keep the four icons/benefit boxes (Guaranteed Payout, Free Evaluations, Affordable Solutions, Industry Leaders) in the same order. Update the icons to cleaner, more modern styles — but maintain the same meanings. Improve alignment and spacing for sharper visual consistency. 6. Remove Icons in Contact Area At the bottom (“CALL TEXT OR BOOK ONLINE 555-014-2796 TallowRidgeBuilders.example”), remove the phone and internet icons, as noted on page 2 of the PDF. 7. Replace All Images I (Darnell) will provide all updated stock images separately via email. Replace the flood/water-damage imagery and roof leak with the new images I send. Keep image placement and proportions the same as the mock-up. BACK SIDE INSTRUCTIONS 1. Header Image + “REFER / EARN” Section Maintain the same large split-image layout (“The more you refer, the more you earn”). Replace all background imagery with the new assets I will send. Keep the CASH FLOW image section but modernize the type and spacing. 2. “HOW IT WORKS” Section Preserve the three-column layout: Refer Flood, Water & Mold Damage We Take Care of Everything (evaluations/insurance) Get Paid to Share Update images, tighten spacing, and use modern iconography. 3. Remove Phone/Internet Icons Same as the front side — remove small communication icons and keep only the text/number/URL. 4. Bottom Contact Bar Keep the blue bar, same wording, same layout — just modernize the style if needed for clarity. 5. Replace All Back-Side Images Again, I will email you the image assets. Keep the layout EXACT — just update with higher-quality photos and improved design. TEXT CONTENT (Keep as-is unless spacing adjustments needed) All text shown in the PDF should remain exactly the same unless spacing or visual balance requires minor adjustments. Example from page 3: “REFER FLOOD, MOLD & CONSTRUCTION JOBS” “We Schedule a Free Estimate. If Approved, You Get Paid.” “Everybody Benefits From Referrals” Everything stays, just refreshed and visually improved. DESIGN GOALS Flyer should look high-end and trustworthy, not salesy. Consistent color theme: blues, whites, yellows, same palette as original. Use bold, modern fonts with strong readability. Ensure all headlines pop and all benefit boxes are clean, well-aligned, and evenly spaced. The final result should feel like a premium referral program flyer for a top-tier restoration/remodel company. FILES I WILL PROVIDE I will send the designer: All replacement stock photos Any updated logos (if needed) Original high-resolution version of the mock-up (if available) Any additional icons preferred

```html
<!DOCTYPE html>
<html lang="en">
<head>
<meta charset="utf-8">
<title>Referral Partner Program Flyer</title>
<link href="https://fonts.googleapis.com/css2?family=Exo+2:wght@500;600;700;800;900&family=Saira+Condensed:wght@800;900&family=Saira+Semi+Condensed:wght@800;900&display=swap" rel="stylesheet">
<style>
  :root {
    --royal: #0a3fae;
    --royal-deep: #0b3399;
    --navy: #0d2357;
    --gold: #fdb813;
    --gold-dark: #b08a12;
    --white: #ffffff;
    --tile: #eeeeee;
    --page: #ffffff;
  }
  * { margin: 0; padding: 0; box-sizing: border-box; }
  html, body { width: 1200px; height: 1200px; overflow: hidden; background: var(--page); }
  body { position: relative; font-family: "Exo 2", sans-serif; }

  .flyer {
    position: absolute; left: 219px; width: 770px; height: 499px;
    background: var(--white); overflow: hidden;
    box-shadow: 0 4px 14px rgba(0,0,0,.22);
  }
  .flyer--front { top: 81px; }
  .flyer--back { top: 637px; }
  .abs { position: absolute; }

  .hero-photo {
    position: absolute; left: 0; top: 0; width: 770px; height: 175px;
    background: linear-gradient(180deg, #0b3ba8 0%, #0d48b8 55%, #0a3aa6 100%);
  }
  .flyer--back .hero-photo { height: 236px; background: linear-gradient(100deg, #0a3aa6 0%, #0e4bbd 60%, #0b3ba8 100%); }

  .headline { position: absolute; left: 0; width: 770px; text-align: center; line-height: 1; }
  .headline--earn { top: -5px; font-family: "Saira Semi Condensed", sans-serif; font-size: 78px; font-weight: 900; color: var(--gold); }
  .headline--unlimited { top: 60px; font-family: "Saira Condensed", sans-serif; font-size: 52px; font-weight: 800; color: var(--white); }
  .headline--cash { top: 95px; font-family: "Saira Semi Condensed", sans-serif; font-size: 78px; font-weight: 900; color: var(--gold); }

  .ribbon-wing { position: absolute; top: 0; left: 0; }
  .ribbon {
    position: absolute; left: 141px; width: 488px; height: 54px; background: var(--gold);
    color: var(--navy); font-weight: 800; text-align: center; line-height: 54px;
  }
  .ribbon--front { top: 175px; font-size: 36px; }
  .ribbon--back { top: 236px; font-size: 38px; }

  .offer-band { position: absolute; left: 0; top: 235px; }
  .offer-text { position: absolute; color: var(--gold); font-weight: 800; text-align: center; line-height: 1; font-size: 29px; }
  .offer-or {
    position: absolute; left: 12px; top: 257px; width: 38px; height: 38px; border-radius: 50%;
    background: var(--gold); color: var(--royal); font-weight: 800; font-size: 26px; text-align: center; line-height: 34px;
  }

  .wins { position: absolute; top: 325px; left: 0; width: 770px; display: flex; align-items: center; justify-content: center; gap: 8px; }
  .wins__rule { width: 108px; height: 6px; border-top: 2px solid var(--royal-deep); border-bottom: 2px solid var(--royal-deep); }
  .wins__text { font-size: 26px; font-weight: 800; color: var(--navy); }

  .benefit { position: absolute; top: 362px; width: 182px; height: 58px; overflow: hidden; }
  .benefit--gold { background: var(--gold); color: var(--navy); }
  .benefit--blue { background: var(--royal-deep); color: var(--gold); }
  .benefit__tile { position: absolute; right: 0; top: 0; }
  .benefit__text { position: absolute; left: 6px; top: 6px; font-size: 10.4px; font-weight: 500; line-height: 15px; white-space: nowrap; }
  .benefit__title { font-weight: 600; text-transform: uppercase; font-size: 11px; }

  .tagline { position: absolute; left: 0; width: 770px; text-align: center; font-weight: 800; color: var(--navy); font-size: 24px; line-height: 1; }
  .flyer--front .tagline { top: 430px; }
  .flyer--back .tagline { top: 424px; }

  .contact-bar {
    position: absolute; left: 0; top: 459px; width: 770px; height: 40px; background: var(--royal-deep);
    font-weight: 800; line-height: 40px;
  }
  .contact-bar span { position: absolute; top: 0; white-space: nowrap; }
  .contact-bar__cta { left: 11px; color: var(--gold); font-size: 20px; }
  .contact-bar__phone { left: 345px; color: var(--white); font-size: 16px; font-weight: 700; }
  .contact-bar__sep { left: 474px; color: var(--white); font-size: 18px; font-weight: 500; }
  .contact-bar__web { right: 12px; color: var(--white); font-size: 14px; font-weight: 700; }

  .money-photo {
    position: absolute; left: 388px; top: 0; width: 340px; height: 250px;
    background: radial-gradient(ellipse at 50% 50%, #e6ebe2 0%, #c9d3c6 45%, #9fae9f 68%, rgba(14,75,189,0) 72%);
  }
  .refer-stack { position: absolute; left: 62px; top: 14px; width: 290px; font-weight: 900; line-height: 1; z-index: 2; }
  .refer-stack div { white-space: nowrap; }
  .refer-stack__small { color: var(--white); font-size: 32px; letter-spacing: 5px; }
  .refer-stack__big { color: var(--gold); letter-spacing: 8px; }

  .cash-flow {
    position: absolute; left: 372px; top: 90px; width: 380px; text-align: center;
    font-family: "Saira Semi Condensed", sans-serif; font-weight: 900; font-size: 58px; color: var(--gold);
    -webkit-text-stroke: 1.5px #5a3d00; text-shadow: 0 2px 4px rgba(0,0,0,.4); line-height: 1;
  }

  .step { position: absolute; top: 302px; width: 235px; height: 109px; background: var(--gold); color: var(--navy); overflow: hidden; }
  .step__tile { position: absolute; right: 0; top: 0; }
  .step__title { position: absolute; left: 12px; top: 12px; font-size: 14px; font-weight: 600; line-height: 18px; text-transform: uppercase; }
  .step__body { position: absolute; left: 15px; top: 52px; font-size: 12.4px; font-weight: 500; line-height: 16.5px; white-space: nowrap; }
</style>
</head>
<body>

<section class="flyer flyer--front">
  <div class="hero-photo" role="img" aria-label="Modern living room photo with blue overlay"></div>
  <svg class="abs" style="left:0;top:0" width="770" height="175" aria-hidden="true">
    <path d="M262 32 C232 70 232 110 258 138" fill="none" stroke="#fdb813" stroke-width="6"/>
    <path d="M250 130 L272 145 L262 120 Z" fill="#fdb813"/>
    <path d="M517 32 C547 70 547 110 521 138" fill="none" stroke="#fdb813" stroke-width="6"/>
    <path d="M529 130 L507 145 L517 120 Z" fill="#fdb813"/>
  </svg>
  <div class="headline headline--earn">EARN</div>
  <div class="headline headline--unlimited">UNLIMITED</div>
  <div class="headline headline--cash">CASH</div>

  <svg class="ribbon-wing" width="770" height="235" aria-hidden="true">
    <polygon points="0,175 141,175 141,229 0,180" fill="#b08a12"/>
    <polygon points="629,175 770,175 770,180 629,229" fill="#b08a12"/>
  </svg>
  <div class="ribbon ribbon--front">Get Paid To Refer A Flood</div>

  <svg class="offer-band" width="770" height="82" aria-hidden="true">
    <polygon points="0,0 366,0 385,82 0,82" fill="#0b3399"/>
    <polygon points="405,0 770,0 770,82 385,82" fill="#0b3399"/>
  </svg>
  <div class="offer-or">or</div>
  <div class="offer-text" style="left:58px;top:246px;width:306px">$500 MINIMUM</div>
  <div class="offer-text" style="left:58px;top:282px;width:306px">10% PER REFERRAL</div>
  <div class="offer-text" style="left:405px;top:246px;width:365px">PREMIER PARTNER</div>
  <div class="offer-text" style="left:405px;top:282px;width:365px">PROGRAM</div>

  <div class="wins"><span class="wins__rule"></span><span class="wins__text">PARTNER WITH US &amp; EVERYBODY WINS!</span><span class="wins__rule"></span></div>

  <div class="benefit benefit--gold" style="left:9px">
    <svg class="benefit__tile" width="34" height="58" aria-hidden="true"><polygon points="34,0 34,58 0,58 0,22" fill="#eeeeee"/>
      <g fill="none" stroke="#222" stroke-width="1.2"><rect x="9" y="26" width="20" height="20"/><rect x="13" y="30" width="12" height="7"/><path d="M5 42 V34 M2 37 L5 34 L8 37"/><path d="M17 46 V52 H27 V46"/></g></svg>
    <div class="benefit__text"><div class="benefit__title">Guaranteed Payout*</div>Minimum $500 or 10% of<br>Total Invoice Paid Fast</div>
  </div>
  <div class="benefit benefit--blue" style="left:198px">
    <svg class="benefit__tile" width="32" height="58" aria-hidden="true"><polygon points="32,0 32,58 0,58 0,22" fill="#eeeeee"/>
      <g fill="none" stroke="#222" stroke-width="1.2"><rect x="4" y="25" width="17" height="27"/><circle cx="24" cy="27" r="5"/><path d="M24 24 V27 H26"/><rect x="8" y="40" width="9" height="8"/><path d="M7 30 H17 M7 34 H15"/></g></svg>
    <div class="benefit__text"><div class="benefit__title">Free Estimates</div>Fast &amp; Free Inspections<br>&amp; Written Estimates</div>
  </div>
  <div class="benefit benefit--gold" style="left:387px">
    <svg class="benefit__tile" width="32" height="58" aria-hidden="true"><polygon points="32,0 32,58 0,58 0,22" fill="#eeeeee"/>
      <g fill="none" stroke="#222" stroke-width="1.2"><circle cx="19" cy="30" r="6"/><path d="M17 36 V40 H21 V36"/><path d="M16 30 L18 32 L22 28"/><path d="M4 48 H11 L19 45 L27 41"/><rect x="2" y="44" width="5" height="8"/></g></svg>
    <div class="benefit__text"><div class="benefit__title">Affordable Solutions</div>Lowest Out of Pocket<br>Costs for Your Customers</div>
  </div>
  <div class="benefit benefit--blue" style="left:577px">
    <svg class="benefit__tile" width="30" height="58" aria-hidden="true"><polygon points="30,0 30,58 0,58 0,22" fill="#eeeeee"/>
      <g fill="none" stroke="#222" stroke-width="1.2"><circle cx="15" cy="28" r="3"/><path d="M11 50 V36 H19 V50"/><circle cx="6" cy="34" r="2.5"/><path d="M3 50 V40 H9 V50"/><circle cx="24" cy="34" r="2.5"/><path d="M21 50 V40 H27 V50"/></g></svg>
    <div class="benefit__text"><div class="benefit__title">Industry Leaders</div>Licensed &amp; Certified Experts<br>Provide 100% Guarantee</div>
  </div>

  <div class="tagline">SEND REFERRALS. GET PAID. GROW YOUR BUSINESS</div>

  <div class="contact-bar">
    <span class="contact-bar__cta">CALL, TEXT OR BOOK ONLINE</span>
    <span class="contact-bar__phone">555-014-2796</span>
    <span class="contact-bar__sep">|</span>
    <span class="contact-bar__web">www.TallowRidgeBuilders.example</span>
  </div>
</section>

<section class="flyer flyer--back">
  <div class="hero-photo" role="img" aria-label="Modern interior photo with blue overlay"></div>
  <div class="money-photo" role="img" aria-label="Fanned stack of hundred-dollar bills"></div>
  <div class="refer-stack">
    <div class="refer-stack__small">THE MORE YOU</div>
    <div class="refer-stack__big" style="font-size:62px;margin-top:2px">REFER</div>
    <div class="refer-stack__small" style="margin-top:2px">THE MORE YOU</div>
    <div class="refer-stack__big" style="font-size:76px">EARN</div>
  </div>
  <div class="cash-flow">CASH FLOW</div>

  <svg class="ribbon-wing" width="770" height="296" aria-hidden="true">
    <polygon points="0,236 141,236 141,290 0,241" fill="#b08a12"/>
    <polygon points="629,236 770,236 770,241 629,290" fill="#b08a12"/>
  </svg>
  <div class="ribbon ribbon--back">HOW IT WORKS</div>

  <div class="step" style="left:16px">
    <svg class="step__tile" width="62" height="109" aria-hidden="true"><polygon points="62,0 62,109 0,109 0,38" fill="#eeeeee"/>
      <g fill="none" stroke="#222" stroke-width="1.3"><circle cx="31" cy="72" r="11"/><circle cx="31" cy="68" r="3.5"/><path d="M25 79 Q31 73 37 79"/><circle cx="14" cy="54" r="4"/><circle cx="48" cy="54" r="4"/><circle cx="14" cy="91" r="4"/><circle cx="48" cy="91" r="4"/><path d="M18 57 L23 63 M44 57 L39 63 M18 88 L23 82 M44 88 L39 82"/></g></svg>
    <div class="step__title">Refer Flood, Mold &amp;<br>Construction Jobs:</div>
    <div class="step__body">It’s Simple to Refer 24/7:<br>Call, Text or Book Online.</div>
  </div>
  <div class="step" style="left:266px">
    <svg class="step__tile" width="62" height="109" aria-hidden="true"><polygon points="62,0 62,109 0,109 0,38" fill="#eeeeee"/>
      <g fill="none" stroke="#222" stroke-width="1.3"><circle cx="23" cy="60" r="4"/><circle cx="31" cy="56" r="4"/><circle cx="39" cy="60" r="4"/><path d="M17 74 Q31 64 45 74"/><path d="M11 66 V82 L23 92 H29 M51 66 V82 L39 92 H33"/><path d="M31 84 L27 80 Q27 76 31 78 Q35 76 35 80 Z"/></g></svg>
    <div class="step__title">We Take Care of<br>Everything:</div>
    <div class="step__body">We Schedule a Free<br>Estimate.<br>If Approved, You Get Paid.</div>
  </div>
  <div class="step" style="left:516px">
    <svg class="step__tile" width="62" height="109" aria-hidden="true"><polygon points="62,0 62,109 0,109 0,38" fill="#eeeeee"/>
      <g fill="none" stroke="#222" stroke-width="1.3"><circle cx="31" cy="62" r="9"/><path d="M31 57 V67 M28 59 H33 Q34 62 31 62 Q28 62 29 65 H34"/><path d="M27 71 L24 80 L31 76 L38 80 L35 71"/><path d="M9 70 V86 L21 94 H27 M53 70 V86 L41 94 H35"/><path d="M15 50 V54 M13 52 H17 M47 50 V54 M45 52 H49"/></g></svg>
    <div class="step__title">Everybody Benefits<br>From Referrals</div>
    <div class="step__body">We Provide Expert Quality<br>Work for Affordable Price.</div>
  </div>

  <div class="tagline">REFER: FLOODS, REMODELS, RENOVATIONS &amp; REPAIRS</div>

  <div class="contact-bar">
    <span class="contact-bar__cta">CALL, TEXT OR BOOK ONLINE</span>
    <span class="contact-bar__phone">555-014-2796</span>
    <span class="contact-bar__sep">|</span>
    <span class="contact-bar__web">www.TallowRidgeBuilders.example</span>
  </div>
</section>

</body>
</html>
```